Flyer-Design für ein Baumhaushotel
Zielgruppe
Baumhaushotel. Hochwertige und gehobene Ausstattung. Fokus Natur und Ruhe.
Naturliebhaber, Großstadtmensch der eine Auszeit sucht
Aufgabenstellung
Flyer dreichfach gefaltet, beidseitig bedruckt
Fotos haben wir hochgeladen, eine höhere Auflösung ist auch vorhanden.
Texte können auch gern von unserer Website genommen werden: waldnest-kojen.de
Nicht zu viel Text, z.B. diesen Text:
evtl einfach nur Stichwörter locker einfügen wie zB (dies ist nur eine Auswahl)
zwischen den Bäumen träumen
in vier Metern Höhe
barrierefreies Baumhaus mit vielen Features
Kaminofen
Bad mit Dusche & WC
Pantry-Küche
gemütlich
Echtholzfußboden
atemberaubende Ausblicke, hoher Komfort und Natur pur.
an einem Seengebiet in der Nähe des Deiches, hinter dem die Elbe in die Nordsee mündet.
eine besondere Auszeit hoch über dem Erdboden
Wenn vom Design sinnvoll, kann man noch Vorteile einbringen wie zB etwas von dieser Auflistung (muss aber auch nicht genannt werden)
! auf jeden Fall soll unser barrierefreies Kiebitz-Baumhaus genannt und gezeigt werden !
30qm Baumhäuser in vier Meter Höhe inkl. Bad und Pantry-Küche, Schlafbereich, Couchecke und Essbereich
10qm Außenterrasse auf 2,50m Höhe inkl. Strandkorb
einzigartiges großes barrierefreies Baumhaus (57qm) , mit barrierefreiem Bad und vielen Features sowie Fußbodenerwärmung, dieses Haus ist für bis zu 6 Personen nutzbar, alle anderen Baumhäuser bis zu 4 Personen
Wlan, TV, Heizung, Kaminofen und voll ausgestattete Küche
Parkplatz direkt im Einfahrtbereich inklusive – das Baumhaushotel-Gelände selbst ist autofrei
haustierfreie und haustierfreundliche Baumhäuser verfügbar
Bettwäsche, Handtücher und Kaminholz inklusive
hoteleigene Kanus und Bootsanleger am Drei-Seengebiet inklusive
von alten Bäumen umgebendes Baumhausgelände inkl. Waldbad (im Sinne von Shinrin Yoku)
Baumhaushotel liegt direkt neben Drei-Seengebiet und in Deichnähe zur Elbe/ Nordsee
spezieller Rückzugsbereich für Tiere, den wir Menschen nicht betreten – Tierbeo..

```html
<!DOCTYPE html>
<html lang="de">
<head>
<meta charset="utf-8">
<title>Baumhaushotel Flyer – Innenseite</title>
<link href="https://fonts.googleapis.com/css2?family=Questrial&display=swap" rel="stylesheet">
<style>
  :root {
    --forest: #363f2c;
    --bark: #4b2c23;
    --olive: #6b6d45;
    --paper: #ecebe8;
    --white: #f4f3f0;
    --rust: #74382a;
    --headline: #dcdad4;
  }
  * { box-sizing: border-box; margin: 0; padding: 0; }
  html, body { width: 1200px; height: 884px; overflow: hidden; background: #e9e6e1; }
  body { font-family: "Questrial", "Helvetica Neue", Arial, sans-serif; }

  .spread { position: relative; width: 1200px; height: 884px; display: flex; }
  .panel { position: relative; width: 400px; height: 884px; overflow: hidden; }

  .photo { position: absolute; }

  /* Panel 1 */
  .panel--intro { background: var(--forest); }
  .photo--living {
    left: 0; top: 0; width: 400px; height: 445px;
    background:
      linear-gradient(180deg, #b47a3e 0%, #c98f4f 18%, #cfcbc4 26%, #c5c2bb 45%, #6d8a8a 60%, #9a6d45 78%, #7a5433 100%);
  }
  .caption {
    position: absolute; background: var(--paper); color: var(--rust);
    font-size: 17px; line-height: 1.3; letter-spacing: 0.2px;
  }
  .caption--intro { left: 0; top: 403px; width: 276px; height: 126px; padding: 34px 0 0 32px; }
  .intro-text {
    position: absolute; left: 34px; top: 628px; width: 320px;
    color: var(--white); font-size: 14.5px; line-height: 1.42; letter-spacing: 0.2px;
  }

  /* Panel 2 */
  .panel--feature { background: var(--bark); }
  .photo--night-left {
    left: 52px; top: 0; width: 348px; height: 206px;
    background: linear-gradient(180deg, #2f4470 0%, #24365a 35%, #141a16 62%, #101410 100%);
  }
  .photo--bedroom {
    left: 110px; top: 443px; width: 290px; height: 441px;
    background: linear-gradient(170deg, #b38350 0%, #c08a68 22%, #a07360 38%, #8d8a88 60%, #b7b7bb 80%, #6b5a4c 100%);
  }
  .band { position: absolute; background: var(--olive); }
  .band--vertical { left: 88px; top: 570px; width: 22px; height: 260px; }
  .band--horizontal-mid { left: 332px; top: 425px; width: 68px; height: 18px; }
  .headline-box {
    position: absolute; left: 52px; top: 254px; width: 280px; height: 322px;
    background: var(--forest); padding: 92px 0 0 34px;
  }
  .headline {
    color: var(--headline); font-weight: 400; font-size: 27px; line-height: 1.22; letter-spacing: 0.6px;
  }

  /* Panel 3 */
  .panel--details { background: var(--white); }
  .photo--night-right {
    left: 0; top: 0; width: 400px; height: 203px;
    background: linear-gradient(180deg, #2f4470 0%, #27395f 45%, #141a16 75%, #101410 100%);
  }
  .photo--stove {
    left: 96px; top: 99px; width: 304px; height: 191px;
    background: linear-gradient(90deg, #d9d5cf 0%, #a98552 28%, #3a3836 55%, #2c2b2a 75%, #dcd9d4 100%);
  }
  .photo--bathroom {
    left: 0; top: 436px; width: 400px; height: 448px;
    background: linear-gradient(175deg, #e7e3de 0%, #d6d1cb 18%, #a57a4d 32%, #6d5a4a 50%, #a7a6a8 66%, #5a3a26 100%);
  }
  .band--horizontal-right { left: 0; top: 425px; width: 80px; height: 18px; }
  .caption--details { left: 96px; top: 305px; width: 304px; height: 164px; padding: 34px 0 0 24px; font-size: 16.5px; }
</style>
</head>
<body>
  <main class="spread">
    <section class="panel panel--intro">
      <div class="photo photo--living" role="img" aria-label="Wohnraum im Baumhaus mit blauer Couchecke, Kaminofen, Holzdecke und Leiter zur Galerie"></div>
      <p class="caption caption--intro">Atemberaubende<br>Ausblicke, hoher Komfort<br>und Natur pur</p>
      <p class="intro-text">Das Baumhaushotel im hohen Norden Deutschlands liegt an einem Seengebiet in der Nähe des Deiches, hinter dem die Elbe in die Nordsee mündet. Unsere Baumhäuser bieten atemberaubende Ausblicke, hohen Komfort und Natur pur. Genießen Sie eine besondere Auszeit hoch über dem Erdboden.</p>
    </section>

    <section class="panel panel--feature">
      <div class="photo photo--night-left" role="img" aria-label="Baumhäuser zwischen Bäumen in der Abenddämmerung"></div>
      <div class="band band--vertical"></div>
      <div class="band band--horizontal-mid"></div>
      <div class="photo photo--bedroom" role="img" aria-label="Schlafbereich mit Doppelbett, Nachttischlampe und Holzdecke"></div>
      <div class="headline-box">
        <h1 class="headline">Eine besondere<br>Auszeithoch<br>über dem<br>Erdboden</h1>
      </div>
    </section>

    <section class="panel panel--details">
      <div class="photo photo--night-right" role="img" aria-label="Baumhaus im Abendlicht vor dunklem Himmel"></div>
      <div class="photo photo--stove" role="img" aria-label="Gusseiserner Kaminofen mit brennendem Feuer neben einer Sitzbank"></div>
      <div class="band band--horizontal-right"></div>
      <div class="photo photo--bathroom" role="img" aria-label="Schlafbereich mit Schiebetür zum Bad mit Dusche und WC"></div>
      <p class="caption caption--details">An einem Seengebiet in<br>der Nähe des Deiches,<br>hinter dem die Elbe in<br>die Nordsee mündet</p>
    </section>
  </main>
</body>
</html>
```